New Product/Company Launch Postcard Design

I need a postcard design for a new product launch/new company called Trinvelas. Trinvelas are decorative ring hooks designed to decorate home fixtures for holidays, seasons and special occasions. The rings have hooks for hanging your favorite hanging ornaments, party decorations or fashionable accessories. Trinvelas comes in 3 sizes; small, medium and large with 4 available colors to accommodate most home fixtures. The rings have a split opening for easy attaching or placing on home fixtures, so there are no tools, no glue, the ring is easily attachable. The rings are simply easy to decorate and easy to create ideas.

I would like the postcard to communicate the product use and would like it to drive customers to my website. On this postcard, I am offering $4.99 2-pack special, Introductory offer. I would also like the postcard to direct them to my website to sign up for specials and offers, by doing so, I will give away a free small Trinvela. Please visit my website at www.trinvelasdesigns.com for other creative ideas.

I had someone create the logo, the colors I chose were black, hot pink and yellow. However, if the logo doesn't seem to work on the design, I am open for comments or other ideas.

```html
<!DOCTYPE html>
<html lang="en">
<head>
<meta charset="utf-8">
<title>Trinvelas Launch Postcard</title>
<link rel="stylesheet" href="https://fonts.googleapis.com/css2?family=Oswald:wght@600&family=Roboto+Condensed:wght@700&family=Courier+Prime:ital@1&family=Lora:ital@1&display=swap">
<style>
  :root {
    --ink: #050505;
    --grid: rgba(255,255,255,0.55);
    --yellow: #f2ef00;
    --yellow-light: #fbfb9a;
    --pink: #f25c8c;
    --hot-pink: #ff6aa0;
    --white: #ffffff;
    --banner: #c9c23e;
    --banner-edge: #6b6720;
    --banner-text: #1e1d08;
  }
  html, body {
    margin: 0;
    padding: 0;
    width: 1200px;
    height: 728px;
    overflow: hidden;
    background: var(--ink);
  }
  .postcard {
    position: relative;
    width: 1200px;
    height: 728px;
    overflow: hidden;
    background-color: var(--ink);
    background-image:
      linear-gradient(var(--grid) 2px, transparent 2px),
      linear-gradient(90deg, var(--grid) 2px, transparent 2px);
    background-size: 24px 24px;
    background-position: 10px 6px;
  }
  .frame-art {
    position: absolute;
    inset: 0;
  }
  .product-band {
    position: absolute;
    left: 0;
    top: 298px;
    width: 1200px;
    height: 196px;
    background: var(--ink);
  }
  .brand-name {
    position: absolute;
    left: 40px;
    top: 226px;
    margin: 0;
    font-family: "Oswald", sans-serif;
    font-weight: 600;
    font-size: 60px;
    letter-spacing: 1px;
    color: var(--white);
    line-height: 1;
  }
  .colour-strip {
    position: absolute;
    left: 64px;
    top: 316px;
    width: 852px;
    height: 160px;
    display: flex;
  }
  .colour-swatch {
    position: relative;
    flex: 1;
  }
  .swatch-bronze { background: linear-gradient(135deg, #cfcac2, #8d877e); }
  .swatch-white { background: linear-gradient(135deg, #6a6864, #2e2c2a); }
  .swatch-stainless { background: linear-gradient(135deg, #8a8884, #4a4844); }
  .swatch-black { background: linear-gradient(135deg, #c9c6c0, #86827c); }
  .swatch-label {
    position: absolute;
    right: 16px;
    bottom: 14px;
    font-family: "Lora", serif;
    font-style: italic;
    font-size: 17px;
    color: #f4f0e6;
    text-shadow: 0 1px 2px rgba(0,0,0,0.6);
  }
  .swatch-bronze .swatch-label { color: #8a6a3a; text-shadow: none; }
  .availability-banner {
    position: absolute;
    left: 334px;
    top: 326px;
    width: 580px;
    height: 44px;
    box-sizing: border-box;
    background: var(--banner);
    border: 2px solid var(--banner-edge);
    font-family: "Courier Prime", monospace;
    font-style: italic;
    font-size: 19px;
    color: var(--banner-text);
    display: flex;
    align-items: center;
    justify-content: center;
    margin: 0;
    white-space: nowrap;
  }
  .offer-price {
    position: absolute;
    left: 944px;
    top: 304px;
    margin: 0;
    font-family: "Roboto Condensed", sans-serif;
    font-weight: 700;
    font-size: 23px;
    color: var(--white);
  }
  .offer-emblem {
    position: absolute;
    left: 956px;
    top: 352px;
    width: 216px;
    height: 170px;
    border-radius: 40px;
    background: var(--hot-pink);
  }
  .signup-call {
    position: absolute;
    left: 240px;
    top: 540px;
    width: 690px;
    margin: 0;
    padding: 6px 12px;
    box-sizing: border-box;
    background: var(--ink);
    font-family: "Roboto Condensed", sans-serif;
    font-weight: 700;
    font-size: 22px;
    line-height: 1.2;
    color: var(--white);
    white-space: nowrap;
  }
  .signup-call .site { color: var(--yellow); }
</style>
</head>
<body>
<main class="postcard">
  <div class="product-band"></div>

  <svg class="frame-art" width="1200" height="728" viewBox="0 0 1200 728" aria-hidden="true">
    <defs>
      <linearGradient id="metal" x1="0" y1="0" x2="0" y2="1">
        <stop offset="0" stop-color="#d8d8d8"/>
        <stop offset="0.5" stop-color="#7c7c7c"/>
        <stop offset="1" stop-color="#bdbdbd"/>
      </linearGradient>
      <linearGradient id="glow" x1="0" y1="0" x2="0" y2="1">
        <stop offset="0" stop-color="#f2ef00"/>
        <stop offset="0.5" stop-color="#fbfb9a"/>
        <stop offset="1" stop-color="#f2ef00"/>
      </linearGradient>
    </defs>

    <rect class="metal-edge" x="0" y="0" width="1200" height="14" fill="url(#metal)"/>
    <rect class="metal-edge" x="0" y="714" width="1200" height="14" fill="url(#metal)"/>

    <g class="top-bracket" fill="url(#glow)">
      <rect x="56" y="16" width="1114" height="60"/>
      <rect x="1120" y="16" width="50" height="180"/>
      <polygon points="1020,145 1120,95 1120,195"/>
    </g>
    <g class="top-pointer" fill="#f25c8c">
      <rect x="56" y="112" width="950" height="5"/>
      <polygon points="1016,114.5 1000,106 1000,123"/>
    </g>

    <g class="bottom-bracket" fill="url(#glow)">
      <rect x="56" y="630" width="1114" height="60"/>
      <rect x="56" y="510" width="50" height="180"/>
      <polygon points="208,560 106,510 106,610"/>
    </g>
    <g class="bottom-pointer" fill="#f25c8c">
      <rect x="216" y="608" width="954" height="5"/>
      <polygon points="204,610.5 220,602 220,619"/>
    </g>
  </svg>

  <h1 class="brand-name">TRINVELAS</h1>

  <div class="colour-strip">
    <div class="colour-swatch swatch-bronze" role="img" aria-label="Photo of three bronze Trinvela ring hooks"><span class="swatch-label">Bronze</span></div>
    <div class="colour-swatch swatch-white" role="img" aria-label="Photo of three white Trinvela ring hooks"><span class="swatch-label">White</span></div>
    <div class="colour-swatch swatch-stainless" role="img" aria-label="Photo of three stainless Trinvela ring hooks"><span class="swatch-label">Stainless</span></div>
    <div class="colour-swatch swatch-black" role="img" aria-label="Photo of three black Trinvela ring hooks"><span class="swatch-label">Black</span></div>
  </div>

  <p class="availability-banner">TRINVELAS now available in 3 sizes and 4 colors!</p>

  <p class="offer-price">$4.99 2-pack special</p>
  <div class="offer-emblem" role="img" aria-label="Pink butterfly illustration formed from ring hooks"></div>

  <p class="signup-call">Sign up at <span class="site">www.trinvelasdesigns.com</span> for specials and get a free small Trinvela!</p>
</main>
</body>
</html>
```